Banner Ad Design Project

We need a 728x90 and a 300x250
1st option
"I have a lead for you. Click here to close the deal."
In large bold letters.
Under this in smaller letters,
"Borwelt. For serious business networkers"
2nd option
"Put that coffee down!"
"Coffee's for closers only."
Close more deals. BORWELT LOGO
(this is a quote from Harrowmere Tavish. It is a famous sales movie)
The other option is
"First you get the money" "Then you get the power" in bold letters.
"Borwelt. For serious business networkers" in smaller letters at the bottom.
-Must have our colors
-Must have our logo (Small at the bottom right)
-Watch the video at borwelt () com
Please be creative. If the banner can have multiple images that would be great as well.
This needs to be a serious looking ad that is bold and clean.
Updates
Please be sure to use the phrase, "Put that coffee down! Coffee's for closers only" with the logo and at the bottom the words, Borwelt, for serious business networkers. in one of the designs. This will be our first campaign. I am looking for a very simple design that is bold. Perhaps just a coffee cup with the words and no other graphics.
Target Market(s)
Sales professionals
Industry/Entity Type
Business
Look and feel

```html
<!DOCTYPE html>
<html lang="en">
<head>
<meta charset="utf-8">
<title>Borwelt – Coffee's for closers banner</title>
<link rel="stylesheet" href="https://fonts.googleapis.com/css2?family=Tinos:wght@700&family=Open+Sans:wght@400&display=swap">
<style>
  :root {
    --page-bg: #ecebe8;
    --card-white: #ffffff;
    --panel-top: #ffffff;
    --panel-bottom: #e9eaec;
    --panel-edge: #d3d5d9;
    --headline-blue: #3a5a9c;
    --accent-orange: #f5a623;
    --logo-slate: #4f6690;
    --cup-light: #f2f3f4;
    --cup-mid: #c9cdd2;
  }
  * { margin: 0; padding: 0; box-sizing: border-box; }
  html, body {
    width: 1200px;
    height: 989px;
    overflow: hidden;
    background: var(--page-bg);
  }
  .canvas {
    position: relative;
    width: 1200px;
    height: 989px;
  }
  .banner {
    position: absolute;
    left: 172px;
    top: 113px;
    width: 918px;
    height: 780px;
    background: var(--card-white);
  }
  .banner-panel {
    position: absolute;
    left: 17px;
    top: 20px;
    width: 885px;
    height: 739px;
    border-radius: 32px;
    border: 2px solid var(--panel-edge);
    background: linear-gradient(180deg, var(--panel-top) 0%, var(--panel-bottom) 100%);
    box-shadow: 0 4px 8px rgba(0, 0, 0, 0.18);
  }
  .headline {
    position: absolute;
    left: 0;
    top: 36px;
    width: 100%;
    text-align: center;
    font-family: "Tinos", "Times New Roman", serif;
    font-weight: 700;
    font-size: 78px;
    line-height: 1;
    color: var(--headline-blue);
  }
  .subhead {
    position: absolute;
    right: 30px;
    top: 162px;
    font-family: "Tinos", "Times New Roman", serif;
    font-weight: 700;
    font-size: 50px;
    line-height: 1;
    color: var(--accent-orange);
  }
  .cup-illustration {
    position: absolute;
    left: 52px;
    top: 252px;
    width: 257px;
    height: 385px;
    border-radius: 40px 40px 60px 60px;
    background: linear-gradient(90deg, var(--cup-mid) 0%, var(--cup-light) 45%, var(--cup-mid) 100%);
  }
  .brand-mark {
    position: absolute;
    right: 34px;
    bottom: 60px;
    display: flex;
    align-items: center;
    gap: 16px;
  }
  .brand-square {
    width: 58px;
    height: 58px;
    background: var(--logo-slate);
  }
  .brand-name {
    font-family: "Open Sans", Arial, sans-serif;
    font-weight: 400;
    font-size: 62px;
    line-height: 1;
    color: var(--logo-slate);
  }
</style>
</head>
<body>
  <main class="canvas">
    <section class="banner">
      <div class="banner-panel">
        <h1 class="headline">Put that coffee down!</h1>
        <p class="subhead">Coffee's for closers only</p>
        <div class="cup-illustration" role="img" aria-label="Illustration of a white takeaway coffee cup with lid, filled with coffee"></div>
        <div class="brand-mark">
          <span class="brand-square"></span>
          <span class="brand-name">borwelt</span>
        </div>
      </div>
    </section>
  </main>
</body>
</html>
```